Clean and modern business cards

Looking for an updated business card design for my dental office “tovrelle dental” . Looking for a modern clean / sleek design . I’m thinking black background but open to seeing other options . One side needs to have an appointment card . Card needs to have logo, dentist name , phone, email , address . I’ve attached couple of cards I thought were cool as well as my logo
Target Market(s)
Dental patients
Industry/Entity Type
Dentistry
Contact Information for Business Card
Phone email address

```html
<!DOCTYPE html>
<html lang="en">
<head>
<meta charset="utf-8">
<title>Tovrelle Dental – Business Cards</title>
<link rel="stylesheet" href="https://fonts.googleapis.com/css2?family=Montserrat:wght@500;700;800&family=Open+Sans:wght@400;600;700&display=swap">
<style>
  :root {
    --bg: #86878a;
    --card-black: #0d0d0d;
    --card-white: #f4f4f2;
    --edge-lime: #7fb21a;
    --ink: #111111;
    --ink-soft: #5a5a5a;
    --rule-purple: #5a1d84;
    --rule-lime: #9cc21c;
    --icon-red: #d8261c;
    --icon-yellow: #f2c419;
    --icon-blue: #1f9bc4;
    --white: #ffffff;
  }
  * { box-sizing: border-box; margin: 0; padding: 0; }
  html, body { width: 1200px; height: 1050px; overflow: hidden; }
  body {
    background: var(--bg);
    font-family: "Open Sans", Arial, sans-serif;
    position: relative;
  }
  .card {
    position: absolute;
    left: 180px;
    width: 840px;
    height: 480px;
    border-bottom: 4px solid var(--edge-lime);
    box-shadow: 0 14px 30px rgba(0,0,0,0.28);
    overflow: hidden;
  }
  .card--back { top: 36px; background: var(--card-black); }
  .card--front { top: 548px; background: var(--card-white); }

  /* back */
  .brand-seal {
    position: absolute;
    left: 50%; top: 50%;
    transform: translate(-50%, -50%);
    display: flex; align-items: center; gap: 18px;
  }
  .brand-seal__dot {
    width: 46px; height: 46px; border-radius: 50%;
    border: 3px solid var(--white);
  }
  .brand-seal__name {
    font-family: "Montserrat", Arial, sans-serif;
    font-weight: 700;
    font-size: 34px;
    letter-spacing: 8px;
    color: var(--white);
    text-transform: uppercase;
  }

  /* front */
  .brand {
    position: absolute; left: 44px; top: 42px;
    display: flex; align-items: center; gap: 14px;
  }
  .brand__dot { width: 52px; height: 52px; border-radius: 50%; background: var(--ink); }
  .brand__name {
    font-family: "Montserrat", Arial, sans-serif;
    font-weight: 800; font-size: 36px; line-height: 1;
    color: var(--ink); text-transform: uppercase; letter-spacing: 1px;
  }
  .appointment {
    position: absolute; left: 70px; top: 210px; width: 330px;
  }
  .appointment__title {
    font-weight: 700; font-size: 21px; color: var(--ink); margin-bottom: 26px;
  }
  .appointment__field {
    display: flex; align-items: baseline; gap: 8px;
    font-size: 18px; color: var(--ink); margin-bottom: 26px;
  }
  .appointment__line { flex: 1; border-bottom: 2px dotted #444; }

  .contact {
    position: absolute;
    left: 560px; top: 456px;
    width: 420px; height: 250px;
    transform: rotate(-90deg);
    transform-origin: top left;
    color: var(--ink-soft);
  }
  .contact__name {
    font-family: "Montserrat", Arial, sans-serif;
    font-weight: 700; font-size: 27px; text-transform: uppercase;
    letter-spacing: 1px; color: #4c4c4c; line-height: 1.15;
  }
  .contact__role { font-size: 17px; color: #333; }
  .contact__rule { height: 2px; width: 300px; margin: 8px 0; }
  .contact__rule--purple { background: var(--rule-purple); }
  .contact__rule--lime { background: var(--rule-lime); width: 240px; }
  .contact__address { font-size: 17px; line-height: 1.3; color: #333; }
  .contact__list { list-style: none; font-size: 17px; line-height: 1.35; color: #333; }
  .contact__list li { display: flex; align-items: center; gap: 10px; letter-spacing: 1px; }
  .contact__list svg { width: 14px; height: 14px; flex: none; }
</style>
</head>
<body>

<section class="card card--back" aria-label="Card back">
  <div class="brand-seal">
    <span class="brand-seal__dot"></span>
    <span class="brand-seal__name">Tovrelle Dental</span>
  </div>
</section>

<section class="card card--front" aria-label="Card front">
  <div class="brand">
    <span class="brand__dot"></span>
    <span class="brand__name">Tovrelle Dental</span>
  </div>

  <div class="appointment">
    <p class="appointment__title">Your Next Appointment</p>
    <p class="appointment__field">Time: <span class="appointment__line"></span></p>
    <p class="appointment__field">Date: <span class="appointment__line"></span></p>
  </div>

  <div class="contact">
    <p class="contact__name">Dr. Elsen Marquill</p>
    <p class="contact__role">Director</p>
    <div class="contact__rule contact__rule--purple"></div>
    <p class="contact__address">418 Brennick Hwy,<br>Winnipeg, MB</p>
    <div class="contact__rule contact__rule--lime"></div>
    <ul class="contact__list">
      <li>
        <svg viewBox="0 0 14 14" aria-hidden="true"><path d="M3 1 L5 4 L4 5.5 Q5.5 8.5 8.5 10 L10 9 L13 11 L11.5 13 Q5 12 1 3 Z" fill="var(--icon-red)"/></svg>
        204-555-0172
      </li>
      <li>
        <svg viewBox="0 0 14 14" aria-hidden="true"><rect x="1" y="3" width="12" height="8" fill="var(--icon-yellow)"/><path d="M1 3 L7 8 L13 3" stroke="#8a6b00" stroke-width="1" fill="none"/></svg>
        contact@tovrellewpg.ca
      </li>
      <li>
        <svg viewBox="0 0 14 14" aria-hidden="true"><circle cx="7" cy="7" r="6" fill="var(--icon-blue)"/><path d="M1 7 H13 M7 1 V13" stroke="#fff" stroke-width="0.8"/></svg>
        www.tovrellewpg.ca
      </li>
    </ul>
  </div>
</section>

</body>
</html>
```